Presentation card Venture KELO - Tech Incubator from Perú

We need a Design to promote the incubator of technology Startups.
We are in Perú, we work with a string tech filter and develop enterprenurship competencies in the Startup team.
The card is to facilitators and staff memebers of VentureKELO.
We want a clear, modern, tech and agile Design.

We work to help New enterprises of technology here in Perú, we expect the candidates have a big competencies to Research and develop technological products.

We work using methodologies from QRB, Folmestry, Brakewell and Harrowgate univeesities. Our book base is the disciplina of enterpreneur.

We work events all year using diferent formats: Brightforge, Vorne price, OPRA Model Competition you can use these logros in your Design.

Set the name, role, email, cell phone number, address.

Example:
// Contact info section
Tobías Quiroveda
Swift Modeling Hub Manager
tobias.quiroveda@kelo-example.pe
(511) 999 000 417

// Address info section
VentureKELO
Technology-based business incubator
Av. Los Cedrales 884, Valdora
Lima - Perú
web: venture-kelo-example.org.pe
email: venture@kelo-example.pe
phone number: (511) 3926508 ext. 4418

// (optional)Lema section
Making happy using technology

// Social network section
facebook: venturekelooficial

Target Market(s)

Enterprenurship, CTO, Investors, Companies interested on open innovation services

Industry/Entity Type

Information Technology

Contact Information for Business Card

Name, Role, Email, Cell phone number

Colors

Designer to choose colors to be used in the design.

Requirements
Must have
• Logo forms and colors
Nice to have
• I add pictures of the leaders of incubator
Should not have
• No vertical designs

```html
<!DOCTYPE html>
<html lang="en">
<head>
<meta charset="utf-8">
<title>Venture KELO – Business Card</title>
<link href="https://fonts.googleapis.com/css2?family=Montserrat:wght@400;500;700;800&display=swap" rel="stylesheet">
<style>
  :root {
    --page: #ecebe9;
    --card-front: #dcdde0;
    --card-back: #4b484c;
    --accent: #c3395c;
    --ink: #2d2b2d;
    --white: #ffffff;
    --photo-frame: #d9a3a3;
    --photo-a: #b38a63;
    --photo-b: #6f6a6e;
  }
  * { box-sizing: border-box; margin: 0; padding: 0; }
  html, body { width: 1087px; height: 1200px; overflow: hidden; }
  body {
    background: var(--page);
    font-family: "Montserrat", sans-serif;
    position: relative;
  }
  .card {
    position: absolute;
    left: 71px;
    width: 945px;
    height: 540px;
  }
  .card--front { top: 40px; background: var(--card-front); color: var(--ink); }
  .card--back { top: 620px; background: var(--card-back); color: var(--white); }

  /* front: brand */
  .brand {
    position: absolute;
    left: 99px;
    top: 250px;
    display: flex;
    align-items: center;
    gap: 14px;
  }
  .brand__mark { width: 22px; height: 22px; background: var(--accent); }
  .brand__name { font-weight: 800; font-size: 44px; color: var(--ink); letter-spacing: 0.5px; }

  /* front: info blocks */
  .info {
    position: absolute;
    left: 472px;
    padding-left: 30px;
    border-left: 2px solid var(--accent);
  }
  .info--company { top: 56px; }
  .info--person { top: 347px; }
  .info__title {
    font-weight: 800;
    font-size: 29px;
    color: var(--accent);
    letter-spacing: 0.5px;
    line-height: 1.1;
  }
  .info__line { font-size: 20px; line-height: 27px; font-weight: 400; }

  .contacts {
    position: absolute;
    left: 502px;
    list-style: none;
  }
  .contacts--company { top: 191px; }
  .contacts--person { top: 428px; }
  .contacts li {
    display: flex;
    align-items: center;
    gap: 16px;
    font-size: 20px;
    line-height: 27px;
  }
  .contacts svg { width: 18px; height: 16px; flex: none; fill: var(--accent); }

  /* back */
  .brand--back {
    left: 0; right: 0; top: 76px;
    justify-content: center;
  }
  .brand--back .brand__name { color: var(--white); font-size: 36px; }
  .brand--back .brand__mark { width: 18px; height: 18px; }

  .photo {
    position: absolute;
    top: 158px;
    height: 222px;
    border: 3px solid var(--photo-frame);
    background: linear-gradient(180deg, var(--photo-b) 0%, #8a8083 45%, var(--photo-a) 100%);
  }
  .photo--left { left: 2px; width: 466px; }
  .photo--right { left: 475px; width: 468px; }

  .achievements {
    position: absolute;
    top: 455px;
    left: 90px;
    display: flex;
    gap: 44px;
    list-style: none;
    font-weight: 700;
    font-size: 22px;
    letter-spacing: 0.3px;
  }
  .achievements li { display: flex; align-items: center; gap: 8px; }
  .achievements li::before {
    content: "";
    width: 11px; height: 11px;
    border-radius: 50%;
    background: var(--white);
  }
</style>
</head>
<body>

<section class="card card--front">
  <div class="brand">
    <span class="brand__mark"></span>
    <span class="brand__name">Venture KELO</span>
  </div>

  <div class="info info--company">
    <h1 class="info__title">VENTUREKELO</h1>
    <p class="info__line">Technology-based business incubator</p>
    <p class="info__line">Av. Los Cedrales 884, Valdora</p>
    <p class="info__line">Lima - Perú</p>
  </div>
  <ul class="contacts contacts--company">
    <li><svg viewBox="0 0 16 16"><circle cx="8" cy="8" r="7" fill="none" stroke="#c3395c" stroke-width="1.6"/><path d="M1 8h14M8 1c-3 3-3 11 0 14M8 1c3 3 3 11 0 14" fill="none" stroke="#c3395c" stroke-width="1.4"/></svg>venture-kelo-example.org.pe</li>
    <li><svg viewBox="0 0 18 14"><rect x="0" y="1" width="18" height="12"/><path d="M0 1l9 7 9-7" fill="none" stroke="#dcdde0" stroke-width="1.5"/></svg>venture@kelo-example.pe</li>
    <li><svg viewBox="0 0 16 16"><path d="M3 1l3 3-2 2c1 2 3 4 5 5l2-2 3 3-2 3C7 14 2 9 1 3z"/></svg>(511) 3926508 ext. 4418</li>
  </ul>

  <div class="info info--person">
    <h2 class="info__title">TOBÍAS QUIROVEDA</h2>
    <p class="info__line">Swift Modeling Hub Manager</p>
  </div>
  <ul class="contacts contacts--person">
    <li><svg viewBox="0 0 18 14"><rect x="0" y="1" width="18" height="12"/><path d="M0 1l9 7 9-7" fill="none" stroke="#dcdde0" stroke-width="1.5"/></svg>tobias.quiroveda@kelo-example.pe</li>
    <li><svg viewBox="0 0 16 16"><path d="M3 1l3 3-2 2c1 2 3 4 5 5l2-2 3 3-2 3C7 14 2 9 1 3z"/></svg>(511) 999 000 417</li>
  </ul>
</section>

<section class="card card--back">
  <div class="brand brand--back">
    <span class="brand__mark"></span>
    <span class="brand__name">Venture KELO</span>
  </div>

  <div class="photo photo--left" role="img" aria-label="Group photo of the incubator team standing in a workshop room"></div>
  <div class="photo photo--right" role="img" aria-label="Group photo of incubator participants gathered in a large meeting room"></div>

  <ul class="achievements">
    <li>BRIGHTFORGE</li>
    <li>VORNE PRICE</li>
    <li>OPRA MODEL COMPETITION</li>
  </ul>
</section>

</body>
</html>
```